Bref créative
Stationary, Envelope, and Business Card Designs for an Accounting/Bookkeeping company
R&K Ledger and Audit Partners, LLC
Professional
Doug M. Prentt
Partner, Chief Financial Officer
41207 Route 53
Lake Verona, FL 33990
dprentt@rkbooksco.com
www.rkbooksco.com
R&K Ledger and Audit Partners, LLC Logo in AI format - full color.
Logo color specifics.

```html
<!DOCTYPE html>
<html lang="en">
<head>
<meta charset="utf-8">
<title>R&amp;K Ledger and Audit Partners – Business Card</title>
<link rel="stylesheet" href="https://fonts.googleapis.com/css2?family=Cormorant+Garamond:wght@500;600&display=swap">
<style>
  :root {
    --page: #eef0f2;
    --card: #ffffff;
    --blue: #1f5fae;
    --blue-deep: #164a8c;
    --green: #7cc242;
    --green-soft: #b6dc8a;
    --ink-light: #ffffff;
    --url-grey: #8a8f96;
    --brand: #1f5fae;
  }
  * { box-sizing: border-box; margin: 0; padding: 0; }
  html, body { width: 1200px; height: 1009px; overflow: hidden; }
  body {
    background: var(--page);
    font-family: "Cormorant Garamond", Georgia, serif;
    font-variant-numeric: lining-nums;
    display: flex;
    flex-direction: column;
    align-items: center;
    justify-content: center;
    gap: 60px;
  }
  .card {
    position: relative;
    width: 700px;
    height: 400px;
    background: var(--card);
    border-radius: 22px;
    overflow: hidden;
    box-shadow: 0 2px 10px rgba(0,0,0,0.12);
  }
  .card-front .brand {
    position: absolute;
    left: 0; right: 0; top: 120px;
    display: flex;
    align-items: center;
    justify-content: center;
    gap: 18px;
  }
  .brand-dot {
    width: 64px; height: 64px;
    border-radius: 50%;
    background: var(--blue);
    flex: none;
  }
  .brand-name {
    color: var(--brand);
    font-weight: 600;
    font-size: 30px;
    line-height: 1.05;
  }
  .brand-name small { display: block; font-size: 17px; letter-spacing: 1px; }
  .card-front .site {
    position: absolute;
    left: 0; right: 0; top: 260px;
    text-align: center;
    color: var(--url-grey);
    font-size: 17px;
    font-weight: 500;
    letter-spacing: 9px;
    text-transform: uppercase;
  }
  .card-back .swoosh { position: absolute; inset: 0; }
  .contact {
    position: absolute;
    left: 34px; top: 58px;
    list-style: none;
    color: var(--ink-light);
    font-size: 13px;
    font-weight: 600;
    letter-spacing: 1.2px;
    text-transform: uppercase;
  }
  .contact li { display: flex; align-items: center; gap: 10px; height: 25px; white-space: nowrap; }
  .contact svg { width: 14px; height: 14px; flex: none; }
  .card-back .brand {
    position: absolute;
    left: 360px; top: 125px;
    display: flex;
    align-items: center;
    gap: 14px;
  }
  .card-back .brand-dot { width: 52px; height: 52px; }
  .card-back .brand-name { font-size: 28px; }
  .card-back .brand-name small { font-size: 15px; letter-spacing: 0.8px; }
  .holder {
    position: absolute;
    right: 40px; bottom: 28px;
    text-align: right;
    color: var(--ink-light);
    text-transform: uppercase;
    letter-spacing: 2px;
    font-weight: 600;
  }
  .holder-name { font-size: 15px; }
  .holder-title { font-size: 12px; margin-top: 3px; }
</style>
</head>
<body>

<section class="card card-front" aria-label="Business card front">
  <div class="brand">
    <span class="brand-dot"></span>
    <p class="brand-name">R&amp;K<small>Ledger and Audit Partners, LLC</small></p>
  </div>
  <p class="site">www.rkbooksco.com</p>
</section>

<section class="card card-back" aria-label="Business card back">
  <svg class="swoosh" viewBox="0 0 700 400" preserveAspectRatio="none" aria-hidden="true">
    <defs>
      <linearGradient id="blueFill" x1="0" y1="0" x2="1" y2="1">
        <stop offset="0" stop-color="#1f5fae"/>
        <stop offset="1" stop-color="#164a8c"/>
      </linearGradient>
    </defs>
    <path d="M0,0 L0,400 L700,400 L700,330 C540,322 350,260 250,0 Z" fill="url(#blueFill)"/>
    <path d="M258,0 C358,258 545,318 700,322" fill="none" stroke="#7cc242" stroke-width="9"/>
    <path d="M274,0 C372,248 555,306 700,310" fill="none" stroke="#b6dc8a" stroke-width="4"/>
  </svg>

  <ul class="contact">
    <li><svg viewBox="0 0 14 14"><path d="M7 1a4 4 0 0 1 4 4c0 3-4 8-4 8S3 8 3 5a4 4 0 0 1 4-4z" fill="#fff"/></svg>41207 Route 53</li>
    <li><svg viewBox="0 0 14 14"></svg>Lake Verona, FL 33990</li>
    <li><svg viewBox="0 0 14 14"><path d="M3 1h3l1 3-2 1a7 7 0 0 0 4 4l1-2 3 1v3a1 1 0 0 1-1 1A11 11 0 0 1 2 2a1 1 0 0 1 1-1z" fill="#fff"/></svg>(863) 555-0142</li>
    <li><svg viewBox="0 0 14 14"><rect x="4" y="1" width="6" height="12" rx="1" fill="#fff"/></svg>(863) 555-0178</li>
    <li><svg viewBox="0 0 14 14"><rect x="2" y="4" width="10" height="7" fill="#fff"/></svg>(863) 555-0190</li>
    <li><svg viewBox="0 0 14 14"><rect x="1" y="3" width="12" height="8" fill="none" stroke="#fff"/><path d="M1 3l6 5 6-5" fill="none" stroke="#fff"/></svg>dprentt@rkbooksco.com</li>
    <li><svg viewBox="0 0 14 14"><circle cx="7" cy="7" r="5.5" fill="none" stroke="#fff"/></svg>www.rkbooksco.com</li>
  </ul>

  <div class="brand">
    <span class="brand-dot"></span>
    <p class="brand-name">R&amp;K<small>Ledger and Audit Partners, LLC</small></p>
  </div>

  <div class="holder">
    <p class="holder-name">Doug M. Prentt</p>
    <p class="holder-title">Partner, Chief Financial Officer</p>
  </div>
</section>

</body>
</html>
```